Corvid Aviation - Learn to Fly

Our customers are people who span all ages and genders that are interested in learning how to fly airplanes for fun or as a career, or who would like to advance their piloting skills.

Flight training we offer:
Private Pilot Certificate
Instrument Rating
Commercial Pilot Certificate
Sport Pilot Certificate: Powered Parachute
Drone Pilot Training

Ground School we offer:
Sport Pilot Ground School
Private Pilot Ground School
Instrument Pilot Ground School
Drone Pilot Ground School

Target Market(s)

Bessemer, Alabama, United States: High school students, college students, career changers. Someone interested in learning to fly for fun or for a career in the United States.

Industry/Entity Type

Aviation

Requirements
Must have
• I would like for you to enjoy some creative freedom here. The feeling and image we want to portray is a professional, but also very exciting and energizing image. The prospective customer and student should see the brochure and be excited to call us or come out for more information on learning how to fly. Our tag line is: "Small Step Today, Giant Leap Tomorrow."
Nice to have
• It would be helpful if you can do some reading or a little research on each of the types of training that we offer so that you will understand what should be included in the brochure. Our goal is to let everyone know who we are, what we offer, and how to contact us.

This may help some with design ideas: The name Corvid Aviation is inspired by the Orbix Skyward space program because the owner of the flight school is a big fan of Orbix and the Skyward mission.

```html
<!DOCTYPE html>
<html lang="en">
<head>
<meta charset="UTF-8">
<title>Corvid Aviation – Learn to Fly</title>
<link rel="stylesheet" href="https://fonts.googleapis.com/css2?family=Poppins:wght@500;600;700&display=swap">
<style>
  :root {
    --gold: #f7c51e;
    --gold-soft: #f3c77a;
    --white: #ffffff;
    --sky-top: #5d4f57;
    --sky-mid: #b4764f;
    --sky-glow: #f2a653;
    --cloud-low: #6d4a38;
    --ground-dark: #2f2420;
    --band: rgba(255, 214, 180, 0.22);
  }
  * { margin: 0; padding: 0; box-sizing: border-box; }
  html, body {
    width: 1200px;
    height: 857px;
    overflow: hidden;
    background: var(--ground-dark);
  }
  .flyer {
    position: relative;
    width: 1200px;
    height: 857px;
    overflow: hidden;
    font-family: "Poppins", sans-serif;
  }
  .sky-photo {
    position: absolute;
    inset: 0;
    background:
      radial-gradient(ellipse 55% 40% at 62% 42%, rgba(255, 196, 110, 0.85), rgba(242, 166, 83, 0) 70%),
      radial-gradient(ellipse 80% 35% at 50% 78%, rgba(150, 95, 65, 0.7), rgba(150, 95, 65, 0) 75%),
      linear-gradient(180deg, var(--sky-top) 0%, var(--sky-mid) 30%, var(--sky-glow) 48%, var(--cloud-low) 72%, var(--ground-dark) 100%);
  }
  .tagline-band {
    position: absolute;
    left: 345px;
    right: 0;
    top: 100px;
    height: 126px;
    background: linear-gradient(90deg, rgba(255, 214, 180, 0) 0%, var(--band) 35%, var(--band) 100%);
  }
  .tagline {
    position: absolute;
    left: 786px;
    top: 118px;
    color: var(--white);
    font-weight: 600;
    font-size: 26px;
    line-height: 1.45;
  }
  .brand-mark {
    position: absolute;
    left: 60px;
    top: 118px;
    display: flex;
    align-items: center;
    gap: 14px;
    color: var(--white);
    font-weight: 600;
    font-size: 28px;
  }
  .brand-mark .dot {
    width: 30px;
    height: 30px;
    border-radius: 50%;
    background: var(--gold);
  }
  .headline {
    position: absolute;
    left: 78px;
    top: 368px;
    color: var(--gold);
    font-weight: 600;
    font-size: 156px;
    line-height: 1.03;
    letter-spacing: 0.07em;
  }
  .headline-rule {
    position: absolute;
    left: 83px;
    top: 705px;
    width: 705px;
    height: 4px;
    background: linear-gradient(90deg, var(--gold-soft) 0%, var(--gold-soft) 60%, rgba(243, 199, 122, 0) 100%);
  }
</style>
</head>
<body>
  <main class="flyer">
    <div class="sky-photo" role="img" aria-label="Photo of a small single-engine propeller plane flying above clouds at golden sunset"></div>
    <div class="tagline-band"></div>
    <div class="brand-mark"><span class="dot"></span><span>Corvid Aviation</span></div>
    <p class="tagline">Small Step Today,<br>Giant Leap Tomorrow</p>
    <h1 class="headline">CORVID<br>AVIATION</h1>
    <div class="headline-rule"></div>
  </main>
</body>
</html>
```